Local Roofing/Construction company business needs new biz card design

We need a new business card design, current cards are from the start of this operation and generic at best. We are a local Construction Company (General Contractor) with a majority of our work originating from insurance claims-exterior finish work is the main focus (Roofs-Siding-Gutters etc). Heavily involved with homeowners and the low ball offers they receive from insurance company's after a insurable event takes place. I have attached some of our original logo file(s) below.

```html
<!DOCTYPE html>
<html lang="en">
<head>
<meta charset="utf-8">
<title>Stoneline Builders – Business Card</title>
<link href="https://fonts.googleapis.com/css2?family=Figtree:wght@400;700&display=swap" rel="stylesheet">
<style>
  :root {
    --bg: #e4e4e4;
    --green: #4caf66;
    --green-dark: #44a75d;
    --green-light: #60c080;
    --ink-dark: #0b1f22;
    --card-white: #f1f1f1;
    --text-grey: #5a5a5a;
  }
  * { margin: 0; padding: 0; box-sizing: border-box; }
  html, body {
    width: 1200px; height: 1200px; overflow: hidden;
    background: var(--bg);
    font-family: "Figtree", "Helvetica Neue", Arial, sans-serif;
  }
  .card {
    position: absolute;
    left: 234px;
    width: 731px;
    height: 418px;
  }
  .card--front {
    top: 160px;
    background: linear-gradient(215deg, var(--green-light) 0%, var(--green) 55%, var(--green-dark) 100%);
    display: flex; align-items: center; justify-content: center;
  }
  .front-brand {
    display: flex; align-items: center; gap: 18px;
  }
  .brand-square {
    width: 46px; height: 46px; background: var(--ink-dark);
  }
  .front-brand__name {
    font-weight: 700; font-size: 50px; color: var(--ink-dark);
    letter-spacing: 0.5px;
  }
  .card--back {
    top: 632px;
    background: linear-gradient(200deg, #f6f6f6 0%, #ececec 60%, #e8e8e8 100%);
  }
  .person { position: absolute; left: 50px; top: 60px; }
  .person__name {
    font-weight: 700; font-size: 31px; color: var(--green); line-height: 1;
  }
  .person__title {
    font-weight: 400; font-size: 19.5px; color: var(--text-grey); margin-top: 12px;
  }
  .back-brand {
    position: absolute; left: 466px; top: 70px;
    display: flex; align-items: center; gap: 10px;
  }
  .back-brand .brand-square { width: 30px; height: 30px; background: var(--green); }
  .back-brand__name {
    font-weight: 700; font-size: 24px; color: var(--green);
  }
  .contact-list {
    position: absolute; left: 49px; top: 288px; list-style: none;
  }
  .contact-list li {
    display: flex; align-items: center; gap: 10px;
    font-size: 20px; color: var(--text-grey); height: 28px;
  }
  .contact-list svg { width: 16px; height: 16px; flex: none; }
  .address {
    position: absolute; left: 466px; top: 316px;
    font-size: 20px; color: var(--text-grey); line-height: 28px; font-style: normal;
  }
</style>
</head>
<body>
  <section class="card card--front">
    <div class="front-brand">
      <span class="brand-square"></span>
      <span class="front-brand__name">Stoneline Builders</span>
    </div>
  </section>

  <section class="card card--back">
    <div class="person">
      <h1 class="person__name">Dalton Reyes</h1>
      <p class="person__title">Founder &amp; Director</p>
    </div>

    <div class="back-brand">
      <span class="brand-square"></span>
      <span class="back-brand__name">Stoneline Builders</span>
    </div>

    <ul class="contact-list">
      <li>
        <svg viewBox="0 0 16 16" aria-hidden="true"><path fill="#4caf66" d="M3.5 1.5l2.2 2.6-1.2 1.6c.9 2 2.3 3.5 4.3 4.4l1.6-1.2 2.6 2.2-1.3 2.1C6.3 13 2.8 9.6 1.3 4.1z"/><path d="M9.5 2.5a4.5 4.5 0 0 1 4 4M9.3 4.6a2.3 2.3 0 0 1 2 2" stroke="#4caf66" stroke-width="1.3" fill="none"/></svg>
        (405)-555-0142
      </li>
      <li>
        <svg viewBox="0 0 16 16" aria-hidden="true"><rect x="1" y="3" width="14" height="10" rx="1" fill="#4caf66"/><path d="M1.5 4l6.5 5 6.5-5" stroke="#f1f1f1" stroke-width="1.3" fill="none"/></svg>
        info@stonelinebuilders.com
      </li>
      <li>
        <svg viewBox="0 0 16 16" aria-hidden="true"><circle cx="8" cy="8" r="7" fill="#4caf66"/><path d="M1 8h14M8 1c-2.5 3-2.5 11 0 14M8 1c2.5 3 2.5 11 0 14" stroke="#f1f1f1" stroke-width="1.1" fill="none"/></svg>
        www.stonelinebuilders.com
      </li>
    </ul>

    <address class="address">
      4780 Birchwood Lane<br>
      Lake Harbor Maine 11300
    </address>
  </section>
</body>
</html>
```